Zielgruppe
Express-Transporte / Sonderfahrten / Speditionsdienstleistungen
Aufgabenstellung
- - - WORDPRESS Design gesucht - - -
seriosität für b2b ; primär werden Kastensprinter und Planensprinter eingesetzt , nur Stock Bilder verwenden die ohne ein Abo gekauft werden können ; die präsentation soll das unternehmen gross aussehen lassen, ((bitte die Powerpoint lediglich für die übersicht der dienstleistungen verwenden.)) Es sollte mit dem Firmenlogo harmonieren. Es wird nach einem komplett neuen Design gesucht. Gerne die Farbtöne des Logo verwenden. Es wird nach einer Onepage gesucht mit einem modernen Design für Wordpress.
Ähnlich wie die derzeitige website https://welmacor-logistik.example jedoch komplett neu.
Weder mit Website Design noch mit dem der powerpoint bin ich stand jetzt zufrieden.
Ich suche hier nach etwas komplett neuem.
Bereits beantwortete fragen:
1.) Zweck: Vorstellung vom Unternehmen und Dienstleistungen
2.) Zielgruppe: Nekunden / Bestandskunden / generelle übersicht der Dienstleistungen
3.) Auf die Landingpage sollen die im grunde alle Leistungen die wir anbieten und zusätzlich noch einen Text dazu quasi ein über uns Text.
4.) Die Bilder können zur Verfügung gestellt werden. Gerne kann hier jedoch auch via Pixalumen bsp. 'bessere' Bilder verwendet werden
5.) Gerne darf die Website heller sein ; keine direkte vorstellung der Farben. Ggf. ähnlich dem derzeitgen Logo in die richtung Rot/Grau .. allerdings gerne hier auch freie entscheidung / kreativität
6.) mir gefallen die Website xyz und xyz gut (link bitte anfragen)
Bei fragen bitte melden.
Erreichbar Montag - Freitag 08.00 - 17.00h

```html
<!DOCTYPE html>
<html lang="de">
<head>
<meta charset="utf-8">
<title>Welmacor – Transportlösungen</title>
<link href="https://fonts.googleapis.com/css2?family=Lato:ital,wght@0,300;0,400;0,700;0,900;1,400;1,700&display=swap" rel="stylesheet">
<style>
:root{
  --red:#c8102e;
  --grey:#58585a;
  --grey-dark:#4a4a4c;
  --text:#666;
  --light:#e2e2e2;
  --white:#fff;
}
*{margin:0;padding:0;box-sizing:border-box}
html,body{width:1200px;height:2625px;overflow:hidden;background:var(--white);font-family:'Lato',sans-serif;color:var(--text)}
.page{position:relative;width:1200px;height:2625px}
.abs{position:absolute}
.bg-shapes{position:absolute;left:0;top:0}
.topbar{top:7px;left:243px;font-size:8.5px;color:#333;display:flex;gap:18px}
.nav{top:7px;left:598px;font-size:8.5px;font-weight:700;color:var(--white);display:flex;gap:14px}
.brand{font-weight:400;color:var(--red);letter-spacing:1px;white-space:nowrap}
.brand-hero{top:46px;left:242px;font-size:40px;line-height:1}
.brand-hero small{display:block;font-size:17px;color:#333;letter-spacing:2px;margin-left:32px;margin-top:4px}
.hero-title{top:138px;left:243px;width:260px;font-size:26px;font-weight:700;line-height:30px;color:var(--text)}
.hero-sub{top:234px;left:243px;width:240px;font-size:9.5px;font-weight:700;color:var(--red);line-height:15px}
.btn{background:var(--red);color:var(--white);font-weight:700;text-align:center;border-radius:2px}
.btn-hero{top:280px;left:244px;width:106px;height:22px;font-size:11px;line-height:22px}
.stat{top:460px;width:180px;text-align:center;color:var(--white)}
.stat .num{font-size:26px;font-weight:700}
.stat svg{display:block;margin:8px auto 6px}
.stat .lbl{font-size:14px}
.h2{font-size:26px;font-weight:700;color:var(--text)}
.about-title{top:648px;left:243px}
.about-title span{font-weight:300}
.about-text{top:695px;left:243px;width:305px;border-left:2px solid var(--red);padding-left:12px;font-size:9.3px;line-height:15px;color:#555}
.about-text .sig{text-align:right;color:var(--red);font-style:italic;font-weight:700;margin-right:24px}
.photo{background:linear-gradient(135deg,#c9a8b6 0%,#7b6c86 35%,#2a2c38 70%,#121319 100%)}
.about-photo{top:654px;left:611px;width:344px;height:231px}
.fleet-title{top:920px;left:0;width:1200px;text-align:center}
.fleet-grid{top:969px;left:242px;width:713px;height:302px;background:var(--light);display:grid;grid-template-columns:1fr 1fr 1fr;grid-template-rows:1fr 1fr;gap:4px;padding:4px}
.vehicle{background:linear-gradient(180deg,#f2f2f2,#c9c9c9)}
.fleet-info{top:950px;left:455px;width:293px;height:190px;color:var(--white);text-align:center;font-size:14px;line-height:22.5px;padding-top:40px}
.fleet-info strong{font-size:15px}
.contact-title{top:1290px;left:0;width:1200px;text-align:center}
.field{height:18px;border:1px solid #e4e4e4;font-size:7px;color:#888;padding:4px 6px}
.tiny{font-size:7px;color:#777}
.btn-form{top:1403px;left:755px;width:125px;height:18px;font-size:10px;line-height:18px}
.logistics-bg{top:1447px;left:0;width:1200px;height:375px;background:linear-gradient(120deg,#6b6f73 0%,#4b4f53 40%,#2f3235 75%,#505457 100%)}
.logistics-title{top:1492px;left:242px;font-size:24px;font-weight:700;color:var(--white)}
.logistics-text{top:1530px;left:243px;width:300px;font-size:9.2px;line-height:15px;font-weight:700;color:var(--white)}
.logistics-text em{display:block}
.services{top:1500px;left:600px;width:356px;height:266px;background:var(--white);border-top:2px solid var(--red);padding:16px 20px;font-size:9px;line-height:15px}
.services .svc{color:var(--red);font-style:italic;font-weight:700;display:flex;justify-content:space-between;width:190px;height:18.7px}
.services p{color:#555;margin-bottom:4px}
.clients-title{top:1855px;left:0;width:1200px;text-align:center;font-size:22px;font-weight:700;color:#f3b5bf}
.client{top:1880px;width:90px;height:80px;background:#d6d6d6;border-radius:8px}
.footer-brand{top:2024px;left:266px;font-size:19px;line-height:1;color:var(--white)}
.footer-text{font-size:9.5px;line-height:15px;color:#b4b4b6;font-weight:700;white-space:nowrap}
.social{left:540px;width:14px;height:14px;background:#ddd;border-radius:2px}
.partner{background:#e9e9e9;border-radius:3px}
.mobile{top:2198px;left:416px;width:178px;height:372px;background:var(--white);overflow:hidden;border:1px solid #ddd}
</style>
</head>
<body>
<div class="page">

<svg class="bg-shapes" width="1200" height="2625" viewBox="0 0 1200 2625">
  <defs>
    <linearGradient id="hero" x1="0" y1="0" x2="1" y2="1">
      <stop offset="0" stop-color="#3d4652"/>
      <stop offset=".45" stop-color="#1d2430"/>
      <stop offset=".7" stop-color="#7a1f2a"/>
      <stop offset="1" stop-color="#2a1618"/>
    </linearGradient>
  </defs>
  <polygon points="0,365 1200,440 1200,612 0,612" fill="#58585a"/>
  <path d="M492,0 C560,250 660,390 820,416 L1200,440 L1200,0 Z" fill="url(#hero)" role="img" aria-label="Foto: Transporter auf nächtlicher Autobahn mit roten Lichtspuren"/>
  <polygon points="0,1983 1200,2020 1200,2150 0,2150" fill="#6e6e70"/>
</svg>

<div class="abs topbar"><span>+49 (0) 5123 45 67 890</span><span>24/7</span><span>kontakt@welmacor.example</span></div>
<div class="abs nav"><span>Über uns</span><span>Fahrzeugflotte</span><span>Leistungen</span><span>Kontakt</span></div>

<div class="abs brand brand-hero">WELMACOR<small>LOGISTIK</small></div>
<h1 class="abs hero-title">Jederzeit perfekte und termingerechte Transportlösungen</h1>
<p class="abs hero-sub">Ob schnell nach Barcelona, sicher nach Malmö oder gekühlt nach ... lassen Sie sich individuell beraten.</p>
<div class="abs btn btn-hero">Anfrage mailen</div>

<div class="abs stat" style="left:246px"><div class="num">2.234 +</div>
<svg width="36" height="34" viewBox="0 0 36 34" fill="none" stroke="#fff" stroke-width="1.5"><circle cx="18" cy="16" r="10"/><circle cx="18" cy="16" r="4"/><path d="M18 2v4M18 26v4M4 16h4M28 16h4"/></svg>
<div class="lbl">Transporte ´21</div></div>
<div class="abs stat" style="left:420px"><div class="num">678 +</div>
<svg width="36" height="34" viewBox="0 0 36 34" fill="none" stroke="#fff" stroke-width="1.5"><circle cx="18" cy="17" r="14"/><ellipse cx="18" cy="17" rx="6" ry="14"/><path d="M4 17h28M6 10h24M6 24h24"/></svg>
<div class="lbl">Kunden europaweit</div></div>
<div class="abs stat" style="left:600px"><div class="num">78 +</div>
<svg width="36" height="34" viewBox="0 0 36 34" fill="none" stroke="#fff" stroke-width="1.5"><rect x="3" y="10" width="20" height="13"/><path d="M23 14h6l4 5v4H23z"/><circle cx="10" cy="25" r="2.5"/><circle cx="27" cy="25" r="2.5"/></svg>
<div class="lbl">Fahrzeuge</div></div>
<div class="abs stat" style="left:782px"><div class="num">32 +</div>
<svg width="36" height="34" viewBox="0 0 36 34" fill="none" stroke="#fff" stroke-width="1.5"><circle cx="18" cy="8" r="4"/><circle cx="8" cy="22" r="3.5"/><circle cx="28" cy="22" r="3.5"/><path d="M2 33c0-5 12-5 12 0M22 33c0-5 12-5 12 0M12 18c0-5 12-5 12 0"/></svg>
<div class="lbl">Menschen im Team</div></div>

<h2 class="abs h2 about-title">Wer ist WELMACOR<span>LOGISTIK</span></h2>
<div class="abs about-text">
  <p>Als gewissenhaftes Inhabergeführtes Unternehmen konzentrieren wir uns auf das machbare ... Zuverlässigkeit und Vertrauen sind unsere Konstante.</p>
  <p>Wir sind stolz darauf, bereits jetzt rückblickend sagen zu können: „Es hat sich gelohnt!“ Unsere Zahlen, sowie der gesunde Wachstum sprechen für uns. Wir haben uns innerhalb kürzester Zeit von einem lokalen Spediteur zu einem Europaweit agierenden In-Time Logistikdienstleister entwickelt. Wir sind für alle Herausforderungen offen und lösen auch unmögliche Aufgaben. Hierbei spielt es keine Rolle ob es sich um Einzelaufträge oder Festtouren handelt. Unser Angebot orientiert sich immer an den Bedürfnissen und Erwartungen unser Kunden.</p>
  <p class="sig">Jonas Brettner &nbsp;| CEO</p>
</div>
<div class="abs photo about-photo" role="img" aria-label="Foto: Hand am Lenkrad während einer Fahrt in der Abenddämmerung"></div>

<h2 class="abs h2 fleet-title">Fahrzeugflotte</h2>
<div class="abs fleet-grid">
  <div class="vehicle" role="img" aria-label="Foto: Planensprinter mit geöffneter Seitenplane"></div>
  <div class="vehicle" role="img" aria-label="Foto: Planenbus mit Hebebühne"></div>
  <div class="vehicle" role="img" aria-label="Foto: Laderaum eines Kastensprinters"></div>
  <div class="vehicle" role="img" aria-label="Foto: dunkler Koffertransporter"></div>
  <div class="vehicle" role="img" aria-label="Foto: Koffer-Lkw mit Ladebordwand"></div>
  <div class="vehicle" role="img" aria-label="Foto: weißer Planentransporter"></div>
</div>
<svg class="abs" style="top:950px;left:455px" width="295" height="192"><polygon points="7,2 285,0 295,190 0,180" fill="#6a6a6c" opacity=".94"/></svg>
<div class="abs fleet-info"><strong>Planenbus mit Hebebühne, Hubwagen</strong><br>Eurostellplätze: 10<br>Lademaße: 480 x 245 x 250 cm<br>Zuladung: 900 KG<br>(auch als Planenbus &nbsp;XL / XXL)</div>

<h2 class="abs h2 contact-title">Lassen Sie sich jetzt beraten</h2>
<div class="abs field" style="top:1337px;left:343px;width:123px">Vor-, Nachname*</div>
<div class="abs field" style="top:1337px;left:480px;width:124px">E-Mail*</div>
<div class="abs field" style="top:1337px;left:617px;width:125px">Telefon*</div>
<div class="abs field" style="top:1337px;left:755px;width:125px">Firma*</div>
<div class="abs tiny" style="top:1362px;left:403px">*Pflichtangaben</div>
<div class="abs tiny" style="top:1362px;left:760px;color:var(--red)">Wie haben Sie von uns erfahren?</div>
<div class="abs field" style="top:1373px;left:343px;width:398px">Ihr Transportwunsch / Ihre Nachricht</div>
<div class="abs field" style="top:1373px;left:755px;width:125px">Internet</div>
<div class="abs tiny" style="top:1401px;left:345px;width:355px;line-height:12px">Ich habe die <u>Datenschutzerklärung</u> zur Kenntnis genommen und akzeptiert. Ich stimme zu, dass meine Formularangaben zur Kontaktaufnahme bzw. zur Bearbeitung meines Anliegens gespeichert werden.</div>
<div class="abs" style="top:1413px;left:693px;width:8px;height:8px;border:1px solid #aaa"></div>
<div class="abs btn btn-form">abschicken &gt;</div>

<div class="abs logistics-bg" role="img" aria-label="Foto: Transporter in Fahrt auf der Landstraße"></div>
<h2 class="abs logistics-title">Time-in-Logistik</h2>
<div class="abs logistics-text">
  <em>Unser Fokus liegt vorallem auf zeitkritischer sowie sensibler Ware.</em>
  Wir sind uns darüber bewusst: Zeit ist Geld -gerade in dem Bereich der In-Time Logistik gilt diese Redewendung doppelt. Im Zentrum unserer Tätigkeit stehen Fahrzeuge mit einer Ladekapazität bis zu 12 Europaletten und einer Zuladung bis 1350 KG. Wir starten direkt nach Beladung und je Transport übernehmen wir ausschließlich Ihre Ware - so verlieren wir keine wertvolle Zeit und das Risiko einer Beschädigung wird minimiert.<br>
  Ihnen steht dabei immer das volle Fahrzeug zur Verfügung! Vor jedem Transport erhalten Sie eine schriftliche Auftragsbestätigung inklusive eines All-In Preises, der voraussichtlichen Zustellzeit sowie alle relevanten Fahrzeug- und Fahrerdaten. Unser mehrsprachiges Team überwacht den gesamten Transport, setzt sich vor der Zustellung nochmal mit Ihrem Empfänger in Verbindung - und informiert diesen über die Ankunft des Fahrers sowie Ihrer Sendung.
</div>
<div class="abs services">
  <div class="svc"><span>Direkt- und Expresstransporte</span><span>-</span></div>
  <p>Wir liefern schnell, flexibel und direkt - das heißt ohne Bei– und Umladung. Ihre zeitkritische Sendung übernehmen wir bundesweit innerhalb von 60 Minuten. Anschließend befördern wir diese auf schnellstmöglichem Weg zu Ihrem gewünschten Empfangsort.</p>
  <div class="svc"><span>Projektlogistik</span><span>+</span></div>
  <div class="svc"><span>Thermo- und Kühltransporte</span><span>+</span></div>
  <div class="svc"><span>Regel und Festtouren</span><span>+</span></div>
  <div class="svc"><span>GPS und Überwachung</span><span>+</span></div>
  <div class="svc"><span>Warentransportversicherung</span><span>+</span></div>
  <div class="svc"><span>Zollabwicklung</span><span>+</span></div>
  <div class="svc"><span>Lieferzeiten</span><span>+</span></div>
  <div class="svc"><span>Transportpreise</span><span>+</span></div>
  <div class="svc"><span>Fahrer:innen</span><span></span></div>
</div>

<div class="abs clients-title">Kunden u.a.</div>
<div class="abs client" style="left:318px;border-radius:50%"></div>
<div class="abs client" style="left:436px"></div>
<div class="abs client" style="left:556px;border-radius:50%"></div>
<div class="abs client" style="left:673px"></div>
<div class="abs client" style="left:792px;border-radius:50%"></div>

<div class="abs brand footer-brand">WELMACOR</div>
<div class="abs footer-text" style="top:2040px;left:384px">Jonas Brettner e.K.</div>
<div class="abs footer-text" style="top:2055px;left:345px">Lindenweg 14<br>12345 Musterstadt<br>Tel. +49 (0) 5123 45 67 890<br>Fax +49 (0) 5123 45 67 8900<br>kontakt@welmacor.example</div>
<div class="abs social" style="top:2040px"></div>
<div class="abs social" style="top:2058px"></div>
<div class="abs social" style="top:2076px"></div>
<div class="abs social" style="top:2094px"></div>
<div class="abs footer-text" style="top:2040px;left:627px">Home<br>FAQ<br>Impressum<br>AGB<br>Datenschutz<br>CookiePolicy</div>
<div class="abs partner" style="top:2040px;left:772px;width:130px;height:20px"></div>
<div class="abs partner" style="top:2076px;left:776px;width:126px;height:22px"></div>

<div class="abs mobile">
  <div style="font-size:6px;color:#333;padding:3px 4px;display:flex;justify-content:space-between"><span>+49 (0) 5123 45 67 890</span><span>kontakt@welmacor.example</span></div>
  <div class="brand" style="font-size:20px;padding:2px 16px">WELMACOR</div>
  <div style="position:absolute;right:8px;top:22px;width:10px;height:8px;border-top:2px solid var(--red);border-bottom:2px solid var(--red)"></div>
  <svg width="178" height="110" style="display:block;margin-top:8px"><path d="M0,0 C20,70 60,100 120,96 L178,86 L178,0 Z" fill="url(#hero)" role="img" aria-label="Foto: Transporter auf nächtlicher Autobahn"/></svg>
  <div style="padding:8px 6px 0;font-size:17px;font-weight:700;line-height:21px">Jederzeit perfekte und termingerechte Transportlösungen</div>
  <div style="padding:4px 8px;font-size:8.5px;font-weight:700;color:var(--red);line-height:14px">Ob schnell nach Barcelona, sicher nach Malmö oder gekühlt nach ... lassen Sie sich individuell beraten.</div>
  <div class="btn" style="margin:6px 0 0 34px;width:104px;height:18px;font-size:9.5px;line-height:18px">Anfrage stellen</div>
  <div style="padding:8px 4px;font-size:16px;font-weight:700">Wer ist WELMACOR</div>
</div>

</div>
</body>
</html>
```